QVN Inquiry Partners PLLC
Law Firm Conducting Investigations
QVN Inquiry Partners PLLC -
Creative Brief
Professional
Dale Morrow
Attorney
21430 SW 3rd Ave, Suite C2-418 Bellevue, WA 98006
dale@qvninquiry-example.com
www.qvninquiry-example.com
I would like the card to be simple, clean and professional. Please use color schemes that match the logo, but don't use too much gold.
The back of the card should be blank.

```html
<!DOCTYPE html>
<html lang="en">
<head>
<meta charset="utf-8">
<title>QVN Inquiry Partners PLLC – Business Card</title>
<link href="https://fonts.googleapis.com/css2?family=Arimo:wght@400;700&family=Cinzel:wght@400&display=swap" rel="stylesheet">
<style>
  :root {
    --card-bg: #ffffff;
    --card-border: #9a9a9a;
    --page-bg: #ffffff;
    --gold-dark: #8a6a1f;
    --gold-mid: #b8943f;
    --gold-light: #eadbaa;
    --brand-brown: #7a5c14;
    --mark-dark: #4a360c;
    --text-dark: #2b2b2b;
    --text-body: #3a3a3a;
    --divider: #2b2b2b;
  }
  * { margin: 0; padding: 0; box-sizing: border-box; }
  html, body {
    width: 1200px;
    height: 689px;
    overflow: hidden;
    background: var(--page-bg);
  }
  .business-card {
    position: relative;
    width: 1200px;
    height: 689px;
    background: var(--card-bg);
    border: 2px solid var(--card-border);
    font-family: "Arimo", Arial, sans-serif;
    color: var(--text-body);
  }
  .gold-band {
    position: absolute;
    left: 88px;
    top: 0;
    width: 124px;
    height: 100%;
    background:
      radial-gradient(ellipse 90px 220px at 50% 55%, rgba(248,236,196,0.85), rgba(248,236,196,0) 100%),
      linear-gradient(90deg, var(--gold-dark) 0%, var(--gold-mid) 30%, var(--gold-light) 50%, var(--gold-mid) 72%, var(--gold-dark) 100%);
  }
  .brand-square {
    position: absolute;
    left: 95px;
    top: 95px;
    width: 110px;
    height: 110px;
    background: var(--mark-dark);
  }
  .brand-divider {
    position: absolute;
    left: 275px;
    top: 42px;
    width: 3px;
    height: 240px;
    background: var(--divider);
  }
  .brand-name {
    position: absolute;
    left: 298px;
    top: 84px;
    font-family: "Cinzel", "Times New Roman", serif;
    font-size: 56px;
    line-height: 66px;
    font-weight: 400;
    color: var(--brand-brown);
    letter-spacing: 1px;
  }
  .person {
    position: absolute;
    left: 300px;
    top: 350px;
    font-size: 37px;
    line-height: 44px;
    color: var(--text-dark);
  }
  .person-name {
    font-weight: 700;
    color: var(--brand-brown);
  }
  .person-sep { margin: 0 8px; }
  .contact {
    position: absolute;
    left: 300px;
    top: 490px;
    font-size: 27px;
    line-height: 38px;
    color: var(--text-body);
    list-style: none;
  }
  .contact .email { margin-bottom: 8px; }
  .website {
    position: absolute;
    right: 40px;
    top: 608px;
    font-size: 28px;
    line-height: 38px;
    font-weight: 700;
    color: var(--brand-brown);
  }
</style>
</head>
<body>
  <main class="business-card">
    <div class="gold-band"></div>
    <div class="brand-square"></div>
    <div class="brand-divider"></div>
    <div class="brand-name">QVN Inquiry<br>Partners</div>

    <p class="person">
      <span class="person-name">Dale Morrow</span><span class="person-sep">|</span><span class="person-title">Attorney</span>
    </p>

    <ul class="contact">
      <li class="phone">425-555-0184</li>
      <li class="email">dale@qvninquiry-example.com</li>
      <li class="address">21430 SW 3rd Ave,<br>Suite C2-418 Bellevue, WA 98006</li>
    </ul>

    <p class="website">www.qvninquiry-example.com</p>
  </main>
</body>
</html>
```